real esate business card with company logo and name

we need a business card design for a real esate company

The company name is Walsh & Brody Pty Ltd, and we have our logo designed and will upload. We want classic or moden feel. Black or white background. looks more textured. Should include folowinginformations
Paul Walsh and Lucy Brody
Sales Agents & Onsite Manager
p: 07 5948 2063
F: 07 5948 2174
M:0461 857 239
3/42 Marlin Crescent, ELLEN GROVE QLD 4078

We want this business card looks professonal. Thank you in advance.

Industry/Entity Type

Real Estate Agent

Contact Information for Business Card

Paul Walsh and Lucy Brody
Onsite Manager & Sales Agents
p: 07 5948 2063
M:0461 857 239

Font styles to use
Serif

Colors
000000
fbfbfb
333333
959595

Requirements
Must have
• company logo and name, black or white back ground

```html
<!DOCTYPE html>
<html lang="en">
<head>
<meta charset="utf-8">
<title>Walsh &amp; Brody Pty Ltd — Business Card</title>
<link rel="stylesheet" href="https://fonts.googleapis.com/css2?family=Arvo:wght@400;700&display=swap">
<style>
  :root {
    --ink: #000000;
    --paper: #fbfbfb;
    --charcoal: #333333;
    --steel: #959595;
    --backdrop: #e6e6e6;
  }
  * { box-sizing: border-box; margin: 0; padding: 0; }
  html, body {
    width: 1200px;
    height: 902px;
    overflow: hidden;
    background: var(--backdrop);
  }
  body {
    display: flex;
    align-items: center;
    justify-content: center;
    font-family: "Arvo", Georgia, serif;
  }
  .business-card {
    position: relative;
    width: 1000px;
    height: 572px;
    border-radius: 26px;
    overflow: hidden;
    background: var(--ink);
    color: var(--paper);
    box-shadow: 0 20px 50px rgba(0,0,0,.25);
  }
  .card-texture {
    position: absolute;
    inset: 0;
    background:
      linear-gradient(115deg, #050505 0%, #1c1c1c 38%, #3a3a3a 48%, #151515 58%, #050505 100%);
  }
  .brand-band {
    position: absolute;
    top: 0;
    right: 0;
    width: 360px;
    height: 330px;
    background: #141414;
    border-bottom-left-radius: 90px;
  }
  .brand-panel {
    position: absolute;
    top: 0;
    right: 0;
    width: 400px;
    height: 270px;
    background: var(--paper);
    border-bottom-left-radius: 135px;
    display: flex;
    flex-direction: column;
    align-items: center;
    justify-content: center;
    gap: 18px;
    padding-left: 40px;
  }
  .brand-mark {
    width: 70px;
    height: 70px;
    background: var(--steel);
  }
  .brand-name {
    font-size: 20px;
    font-weight: 400;
    letter-spacing: 1px;
    color: var(--charcoal);
  }
  .agents {
    position: absolute;
    top: 110px;
    left: 70px;
  }
  .agent-names {
    font-size: 36px;
    font-weight: 400;
    letter-spacing: .5px;
  }
  .agent-role {
    margin-top: 6px;
    font-size: 15px;
    text-align: right;
    color: #d8d8d8;
  }
  .contact-list {
    position: absolute;
    left: 0;
    top: 300px;
    list-style: none;
  }
  .contact-item {
    display: flex;
    align-items: center;
    height: 62px;
    margin-bottom: 22px;
  }
  .contact-icon {
    flex: none;
    width: 140px;
    height: 62px;
    background: var(--charcoal);
    border-radius: 0 31px 31px 0;
    display: flex;
    align-items: center;
    justify-content: flex-end;
    padding-right: 30px;
  }
  .contact-icon svg {
    width: 30px;
    height: 30px;
    fill: none;
    stroke: var(--paper);
    stroke-width: 1.6;
    stroke-linecap: round;
    stroke-linejoin: round;
  }
  .contact-text {
    margin-left: 34px;
    font-size: 24px;
    line-height: 1.2;
    letter-spacing: .5px;
    white-space: nowrap;
  }
</style>
</head>
<body>
  <article class="business-card">
    <div class="card-texture" role="img" aria-label="Glossy black woven brick texture"></div>

    <div class="brand-band"></div>
    <div class="brand-panel">
      <div class="brand-mark"></div>
      <p class="brand-name">WALSH &amp; BRODY PTY LTD.</p>
    </div>

    <header class="agents">
      <h1 class="agent-names">Paul Walsh and Lucy Brody</h1>
      <p class="agent-role">Onsite Manager &amp; Sales Agents</p>
    </header>

    <ul class="contact-list">
      <li class="contact-item">
        <span class="contact-icon">
          <svg viewBox="0 0 24 24" aria-hidden="true"><path d="M12 21s-7-6.5-7-12a7 7 0 0 1 14 0c0 5.5-7 12-7 12z"/><circle cx="12" cy="9" r="2.6"/></svg>
        </span>
        <span class="contact-text">3/42 Marlin Crescent, HAZEL<br>RIDGE QLD 4185</span>
      </li>
      <li class="contact-item">
        <span class="contact-icon">
          <svg viewBox="0 0 24 24" aria-hidden="true"><circle cx="12" cy="12" r="10"/><path d="M8.5 7.5l1.8 1.8-1 1.5a7 7 0 0 0 3 3l1.5-1 1.8 1.8-1.2 1.4c-3.2-.4-6.3-3.5-6.7-6.7z"/></svg>
        </span>
        <span class="contact-text">07 5948 2063</span>
      </li>
      <li class="contact-item">
        <span class="contact-icon">
          <svg viewBox="0 0 24 24" aria-hidden="true"><rect x="6.5" y="2.5" width="11" height="19" rx="2"/><path d="M11 18.5h2"/></svg>
        </span>
        <span class="contact-text">07 5948 2063</span>
      </li>
    </ul>
  </article>
</body>
</html>
```